Anzeigengestaltung für Stellenanzeige
Zielgruppe
Wir sind ein Abrechnungsunternehmen das für Zahnärzte die zahnmedizinische und zahntechnische Abrechnung von extern übernimmt.
Aufgrund einer Erweiterung suchen wir neues Personal welches uns unterstützt. Deshalb benötigen wir einen Stellenanzeige.
Wir suchen Personal - zahnmedizinische Fachangestellte mit Erfahrung in der Abrechnung
Abkürzungen: ZFA oder ZMV beides gewünscht wenn Abrechnungskenntnisse vorhanden sind.
Aufgabenstellung
Bitte Stellenanzeige unserer Website anpassen, www.praxisfeldwerk.de
logo bitte con Website übernehmen.
Moderne Gestaltung
Wir bieten:
-Anstellung Teilzeit oder Vollzeit
-Ein motiviertes und kompetentes Team
-Fort- und Weitermöglichkeiten
-Flexible Arbeits- und Urlaubszeiten
-Attraktive leistungsgerechte Bezahlung
Ihr Profil
Um die Stelle gut ausfüllen zu können, wünschen wir uns von Ihnen:
Abgeschlossene Ausbildung zum/zur Zahnmedizinische Fachangestellte, Zahnmedizinische Verwaltungsfachangestellte (m/w/d)
Selbstständiges Arbeiten und Einsatzbereitschaft
Gute PC-Kenntnisse und sicherer Umgang mit gängigen Office-Anwendungen
Erfahrung in der zahmedizinischen Abrechnung
Sorgfalt, Teamfähigkeit
Engagement und Freude am Beruf
Wir haben Ihr Interesse geweckt dann senden Sie uns Ihre Bewerbung an: k.malvenich@praxisfeldwerk.de
------Beispiel----------
Gerne auch eigene Beispiele....

```html
<!DOCTYPE html>
<html lang="de">
<head>
<meta charset="utf-8">
<title>Stellenanzeige – Praxisfeldwerk</title>
<link href="https://fonts.googleapis.com/css2?family=Jost:wght@300;400;600&display=swap" rel="stylesheet">
<style>
  :root {
    --stone: #8e8a82;
    --stone-light: #a19d95;
    --ink: #1f1e1c;
    --paper: #f4f2ee;
    --night: #161616;
    --night-soft: #262523;
    --sand: #b8b3a8;
  }
  * { margin: 0; padding: 0; box-sizing: border-box; }
  html, body { width: 860px; height: 1200px; overflow: hidden; }
  body {
    font-family: "Jost", sans-serif;
    background: var(--stone);
  }
  .ad {
    position: relative;
    width: 860px;
    height: 1200px;
    background: radial-gradient(ellipse at 35% 25%, var(--stone-light) 0%, var(--stone) 60%, #86827a 100%);
    overflow: hidden;
  }
  .brand {
    position: absolute;
    right: 42px;
    top: 70px;
    text-align: right;
    color: var(--paper);
  }
  .brand-name {
    font-weight: 600;
    font-size: 36px;
    letter-spacing: -1px;
    line-height: 1;
  }
  .brand-tagline {
    margin-top: 10px;
    font-weight: 400;
    font-size: 10.5px;
    letter-spacing: 1.6px;
  }
  .centered {
    position: absolute;
    left: 0;
    width: 860px;
    text-align: center;
  }
  .headline {
    top: 168px;
    font-weight: 600;
    font-size: 36px;
    color: var(--ink);
    letter-spacing: 0.3px;
  }
  .body-text {
    font-weight: 300;
    font-size: 22px;
    line-height: 30.3px;
    color: var(--paper);
  }
  .intro { top: 255px; }
  .section-title {
    font-weight: 600;
    font-size: 22px;
    line-height: 30px;
    color: var(--ink);
  }
  .offer-title { top: 377px; }
  .offer-list { top: 407px; }
  .profile-title { top: 589px; }
  .profile-list { top: 619px; }
  .contact-band {
    position: absolute;
    left: 0;
    top: 943px;
    width: 860px;
    height: 257px;
    background: linear-gradient(135deg, var(--night-soft) 0%, var(--night) 55%, #111 100%);
  }
  .team-photo {
    position: absolute;
    left: 55px;
    top: 15px;
    width: 265px;
    height: 242px;
    background: radial-gradient(ellipse at 50% 55%, #8a7c6a 0%, #4a4238 45%, rgba(22,22,22,0) 75%);
  }
  .contact {
    position: absolute;
    left: 400px;
    width: 376px;
    text-align: center;
  }
  .contact-hook {
    top: 60px;
    font-weight: 600;
    font-size: 22px;
    line-height: 29px;
    color: var(--sand);
  }
  .contact-call {
    top: 147px;
    font-weight: 300;
    font-size: 21px;
    color: var(--paper);
  }
  .contact-mail {
    top: 175px;
    font-weight: 600;
    font-size: 21px;
    color: #fff;
  }
</style>
</head>
<body>
<main class="ad">
  <header class="brand">
    <div class="brand-name">Praxisfeldwerk</div>
    <div class="brand-tagline">Zahnärztliche Abrechnung &amp; Management</div>
  </header>

  <h1 class="centered headline">WIR SUCHEN PERSONAL!</h1>

  <p class="centered body-text intro">
    Zahnmedizinische Fachangestellte mit Erfahrung in der Abrechnung<br>
    Abkürzung: ZFA oder ZMV beides gewünscht, wenn<br>
    Abrechnungskenntnisse vorhanden sind
  </p>

  <h2 class="centered section-title offer-title">WIR BIETEN:</h2>
  <p class="centered body-text offer-list">
    • Anstellung Teilzeit oder Vollzeit<br>
    • Ein motiviertes und kompetentes Team<br>
    • Fort- und Weitermöglichkeiten<br>
    • Flexible Arbeits- und Urlaubszeiten<br>
    • Attraktive leistungsgerechte Bezahlung
  </p>

  <h2 class="centered section-title profile-title">IHR PROFIL:</h2>
  <p class="centered body-text profile-list">
    Um die Stelle gut ausfüllen zu können, wünschen wir uns von Ihnen:<br>
    • Abgeschlossene Ausbildung zum/zur Zahnmedizinische Fachangestellte,<br>
    Zahnmedizinische Verwaltungsfachangestellte (m/w/d)<br>
    • Selbstständiges Arbeiten und Einsatzbereitschaft<br>
    • Gute PC-Kenntnisse und sicherer Umgang mit gängigen<br>
    Office-Anwendungen<br>
    • Erfahrung in der zahmedizinischen Abrechnung<br>
    • Sorgfalt, Teamfähigkeit<br>
    • Engagement und Freude am Beruf
  </p>

  <section class="contact-band">
    <div class="team-photo" role="img" aria-label="Foto von zwei Mitarbeiterinnen in beigen Blazern"></div>
    <p class="contact contact-hook">WIR HABEN IHR INTERESSE<br>GEWECKT?!</p>
    <p class="contact contact-call">Dann senden Sie uns Ihre Bewerbung an:</p>
    <p class="contact contact-mail">k.malvenich@praxisfeldwerk.de</p>
  </section>
</main>
</body>
</html>
```